I already have a logo created by Quillory Makers that I'm very happy with. I need to spruce up my business card now. Its a double sided card with not much info on it, I like to keep it simple.
Front of card: name, phone # email address, web address. Tag Line "Outsourced Technology Solutions", under that it says Business Voice Services & Electronic Protection.
Rear of Card: Content written inside a "cloud" saying "Cloud Solutions" "Cloud Integrity"

Target Market(s)

Business to Business

Industry/Entity Type

Business

Contact Information for Business Card

We are in the technology field. Providing Telephone systems (hardware), SIP Trunks (dial tone/local/long distance/telephone #'s), LAN (Local Area Network)infrastructure cabling, Data Center solutions and Security Applications (Camera systems, Access Control systems,

Requirements
Must have
• Must have brevity
Should not have
• Clutter and/or too much information

```html
<!DOCTYPE html>
<html lang="en">
<head>
<meta charset="utf-8">
<title>Norvale Signal Works – Business Card</title>
<link rel="stylesheet" href="https://fonts.googleapis.com/css2?family=Open+Sans:wght@300;400;600&display=swap">
<style>
  :root {
    --canvas: #e9e7e3;
    --dark-card: #2f3b47;
    --dark-card-edge: #24303b;
    --cloud-dark: rgba(255, 255, 255, 0.05);
    --light-card: #f4f4f4;
    --cloud-light: rgba(0, 0, 0, 0.035);
    --brand-blue: #1f5fbf;
    --rule-light: #c9ced4;
    --rule-dark: #8a9098;
    --muted-dark: #b9c0c8;
    --muted-light: #8d9197;
    --ink: #2a2f35;
  }
  * { box-sizing: border-box; margin: 0; padding: 0; }
  html, body {
    width: 1200px; height: 1023px; overflow: hidden;
    background: var(--canvas);
    font-family: "Open Sans", Arial, sans-serif;
  }
  .canvas { position: relative; width: 1200px; height: 1023px; }

  .card {
    position: absolute;
    width: 560px; height: 320px;
    border-radius: 18px;
    overflow: hidden;
    box-shadow: 0 14px 30px rgba(0,0,0,0.18);
  }
  .card .clouds { position: absolute; inset: 0; }

  /* Rear side */
  .card-rear {
    left: 60px; top: 90px;
    background: radial-gradient(ellipse at 65% 40%, #3c4955 0%, var(--dark-card) 55%, var(--dark-card-edge) 100%);
  }
  .rear-content {
    position: absolute; left: 150px; top: 88px; width: 340px;
  }
  .brand-name {
    font-weight: 600;
    color: var(--brand-blue);
    line-height: 1.05;
  }
  .card-rear .brand-name { font-size: 30px; }
  .brand-dot {
    display: inline-block; width: 12px; height: 12px; border-radius: 50%;
    background: var(--brand-blue); margin-right: 10px; vertical-align: middle;
  }
  .rule { height: 2px; margin: 10px 0 8px; }
  .card-rear .rule { background: var(--rule-dark); }
  .tagline { font-weight: 300; }
  .card-rear .tagline { color: var(--muted-dark); font-size: 19px; }
  .services {
    list-style: none; display: flex; gap: 18px;
    margin-top: 26px; color: var(--muted-dark); font-size: 15px; font-weight: 300;
  }
  .services li::before {
    content: ""; display: inline-block; width: 6px; height: 6px; border-radius: 50%;
    background: var(--brand-blue); margin-right: 6px; vertical-align: middle;
  }

  /* Front side */
  .card-front {
    left: 580px; top: 590px;
    background: linear-gradient(160deg, #ffffff 0%, var(--light-card) 55%, #e4e5e7 100%);
  }
  .front-brand { position: absolute; right: 34px; top: 34px; width: 300px; }
  .card-front .brand-name { font-size: 24px; }
  .card-front .rule { background: var(--rule-light); }
  .card-front .tagline { color: var(--muted-light); font-size: 15px; }
  .person { position: absolute; left: 250px; top: 160px; }
  .person-name { color: var(--brand-blue); font-size: 24px; font-weight: 400; }
  .person-title { color: var(--muted-light); font-size: 13px; font-weight: 300; margin-top: 2px; }
  .contact {
    position: absolute; left: 34px; bottom: 30px;
    display: grid; grid-template-columns: auto auto; column-gap: 26px; row-gap: 8px;
    font-size: 13px;
  }
  .contact-item { display: flex; align-items: center; gap: 7px; color: var(--ink); }
  .contact-item.link { color: var(--brand-blue); }
  .contact-item svg { width: 13px; height: 13px; flex: none; }
</style>
</head>
<body>
<main class="canvas">

  <section class="card card-rear" aria-label="Card rear">
    <svg class="clouds" viewBox="0 0 560 320" aria-hidden="true">
      <g fill="var(--cloud-dark)">
        <circle cx="250" cy="250" r="110"/>
        <circle cx="370" cy="160" r="140"/>
        <circle cx="500" cy="110" r="110"/>
        <rect x="250" y="160" width="310" height="200"/>
      </g>
    </svg>
    <div class="rear-content">
      <div class="brand-name"><span class="brand-dot"></span>Norvale Signal Works, LLC</div>
      <div class="rule"></div>
      <div class="tagline">Outsourced Technology Solutions</div>
      <ul class="services">
        <li>Cloud Solutions</li>
        <li>Cloud Integrity</li>
      </ul>
    </div>
  </section>

  <section class="card card-front" aria-label="Card front">
    <svg class="clouds" viewBox="0 0 560 320" aria-hidden="true">
      <g fill="var(--cloud-light)">
        <circle cx="70" cy="40" r="80"/>
        <circle cx="170" cy="10" r="90"/>
        <circle cx="470" cy="330" r="100"/>
        <circle cx="380" cy="360" r="80"/>
      </g>
    </svg>
    <div class="front-brand">
      <div class="brand-name"><span class="brand-dot"></span>Norvale Signal Works, LLC</div>
      <div class="rule"></div>
      <div class="tagline">Outsourced Technology Solutions</div>
    </div>
    <div class="person">
      <div class="person-name">Your Name</div>
      <div class="person-title">Title</div>
    </div>
    <div class="contact">
      <div class="contact-item">
        <svg viewBox="0 0 12 12"><path d="M6 0.5a4 4 0 0 0-4 4c0 3 4 7 4 7s4-4 4-7a4 4 0 0 0-4-4z" fill="#7a7f86"/><circle cx="6" cy="4.5" r="1.4" fill="#fff"/></svg>
        Your address
      </div>
      <div class="contact-item link">
        <svg viewBox="0 0 12 12"><rect x="0.7" y="2.2" width="10.6" height="7.6" fill="none" stroke="#7a7f86"/><path d="M0.7 2.2 6 6.8l5.3-4.6" fill="none" stroke="#7a7f86"/></svg>
        info@yourweb.com
      </div>
      <div class="contact-item">
        <svg viewBox="0 0 12 12"><circle cx="6" cy="6" r="5.3" fill="none" stroke="#7a7f86"/><path d="M4 3.3c-.6.6-.6 1.8.6 3.2 1.3 1.5 2.6 1.9 3.2 1.3l.5-.6-1.2-1-.6.5c-.5-.2-1.2-.9-1.5-1.5l.5-.6-1-1.2z" fill="#7a7f86"/></svg>
        (555) 014-3382
      </div>
      <div class="contact-item link">
        <svg viewBox="0 0 12 12"><circle cx="6" cy="6" r="5.3" fill="none" stroke="#7a7f86"/><ellipse cx="6" cy="6" rx="2.3" ry="5.3" fill="none" stroke="#7a7f86"/><path d="M0.7 6h10.6" stroke="#7a7f86"/></svg>
        www.yourweb.com
      </div>
    </div>
  </section>

</main>
</body>
</html>
```